Product Label Design

Need a product design for our Epsom salt product, needs to have a luxurious simple feel to it. The picture attached is our brand and wordage on it, the bag we think should be a stand up bag that should be offwhite/creme color. The other picture are products that we like. We updated the packaging to be a Kraft tube box, please see the attached photo for dimensions.

```html
<!DOCTYPE html>
<html lang="en">
<head>
<meta charset="UTF-8">
<title>Brume Uplift Epsom Salt Label</title>
<link href="https://fonts.googleapis.com/css2?family=Open+Sans:wght@400;600;700&display=swap" rel="stylesheet">
<style>
  :root {
    --page: #f7f7f7;
    --label: #f1efea;
    --seam: #dcd9d2;
    --ink: #141414;
    --accent: #6cc3e2;
    --band: #74cde9;
  }
  * { margin: 0; padding: 0; box-sizing: border-box; }
  html, body {
    width: 1200px;
    height: 1200px;
    overflow: hidden;
    background: var(--page);
    font-family: "Open Sans", sans-serif;
  }
  .canvas {
    position: relative;
    width: 1200px;
    height: 1200px;
  }
  .label {
    position: absolute;
    left: 400px;
    top: 84px;
    width: 400px;
    height: 978px;
    background: var(--label);
    border-radius: 6px;
    overflow: hidden;
  }
  .lid-seam {
    position: absolute;
    left: 0;
    top: 276px;
    width: 100%;
    height: 2px;
    background: var(--seam);
  }
  .brand-name {
    position: absolute;
    top: 395px;
    width: 100%;
    text-align: center;
    font-weight: 700;
    font-size: 84px;
    letter-spacing: 1px;
    color: var(--ink);
  }
  .variant {
    position: absolute;
    top: 552px;
    width: 100%;
    text-align: center;
    font-weight: 700;
    font-size: 28px;
    letter-spacing: 7px;
    color: var(--accent);
  }
  .ingredients {
    position: absolute;
    top: 655px;
    width: 100%;
    text-align: center;
    list-style: none;
    font-size: 17px;
    line-height: 30px;
    color: var(--ink);
  }
  .net-weight {
    position: absolute;
    top: 910px;
    width: 100%;
    text-align: center;
    font-size: 14px;
    letter-spacing: 1.5px;
    color: var(--ink);
  }
  .base-band {
    position: absolute;
    left: 0;
    bottom: 0;
    width: 100%;
    height: 40px;
    background: var(--band);
  }
</style>
</head>
<body>
  <main class="canvas">
    <section class="label">
      <div class="lid-seam"></div>
      <h1 class="brand-name">Brume</h1>
      <h2 class="variant">UPLIFT</h2>
      <ul class="ingredients">
        <li>US Sourced Pure Epsom Salt</li>
        <li>(Magnesium Sulfate)</li>
        <li>+ Abies sibirica</li>
        <li>+ Fir Balsam</li>
      </ul>
      <p class="net-weight">NET WT. 3 LBS (1360 G)</p>
      <div class="base-band"></div>
    </section>
  </main>
</body>
</html>
```